Short Line Railroad website - small company simple homepage

We are looking for someone to design a webpage/home page for our railroad. Doesn't have to be fancy, just basic contact info and links to our regional partners and government agencies. We don't do any online sales but would like a web presence that makes us look professional. We have a logo, and some pictures, but are open to purchasing pictures or other graphical elements to enhance this site. We would like links to our partners websites and emergency information. I don't know how many pages this will take??

Target Market(s)

The website is for our existing customers and their partners, potential new rail customers, regional partners like Ports or Economic Development Agencies, and government regulators. We also need emergency contact info and instructions for the general public.

Industry/Entity Type

It Company

Coding

Coded - Design and coding required

Number of Pages Required

2 page

Font styles to use
Sans Serif

Requirements
Must have
• Our logo - map of railroad and area - some photos - contact info - links to designated partners - emergency contact info and emergency instructions.
• Partners include Harlow County Washington
• Port of Elmstead (Washington)
• MVBTA
• City of Pinecrest Hollow
• National Trackway Bureau
• QBO
• HPMRA
• will add more when I have time
Nice to have
• It would be nice to mostly use our company colors - red, black, and white.
• Just a very professional looking website, with the option of making changes in house in the future.
Should not have
• No ads

```html
<!DOCTYPE html>
<html lang="en">
<head>
<meta charset="utf-8">
<title>Cascade Ridge Junction Railroad</title>
<link rel="stylesheet" href="https://fonts.googleapis.com/css2?family=Open+Sans:wght@400;600;700&family=Roboto+Slab:wght@300;400;700&family=Arvo:wght@400;700&display=swap">
<style>
:root{
  --red:#d42a12;
  --ink:#222;
  --nav:#272727;
  --band:#2e2e2e;
  --footer:#1b1b1b;
  --white:#fff;
  --muted:#666;
  --slab:"Roboto Slab","Arvo","Rockwell","Roboto Slab Regular",serif;
  --sans:"Open Sans","Segoe UI",Arial,sans-serif;
}
*{margin:0;padding:0;box-sizing:border-box}
html,body{width:1200px;height:2356px;overflow:hidden}
body{position:relative;font-family:var(--sans);color:var(--ink);background:var(--white)}
.abs{position:absolute}

.topbar{left:0;top:0;width:1200px;height:42px;background:var(--red);color:var(--white);font-size:11px}
.social{left:132px;top:16px;display:flex;gap:15px}
.social i{width:10px;height:10px;border:1.6px solid var(--white);border-radius:2px;display:block}
.topbar .info{right:133px;top:14px}

.header{left:0;top:42px;width:1200px;height:118px;background:var(--white)}
.logo{left:132px;top:22px;display:flex;align-items:center;gap:10px}
.logo-mark{width:62px;height:62px;background:var(--red)}
.logo-name{color:var(--red);font-weight:700;font-size:20px;line-height:25px}
.contact-btn{left:851px;top:32px;width:216px;height:44px;border:2px solid var(--red);padding:3px}
.contact-btn div{width:100%;height:100%;background:var(--nav);color:var(--white);font-size:12px;display:flex;align-items:center;justify-content:center;gap:6px}

.nav{left:0;top:160px;width:1200px;height:55px;background:var(--nav)}
.nav a{position:absolute;top:0;height:55px;line-height:55px;color:var(--white);font-size:12px;text-decoration:none;font-family:var(--slab)}
.nav .active{left:132px;width:102px;background:var(--red);text-align:center}
.nav .search{left:1008px;top:0;width:59px;height:55px;background:#111;display:flex;align-items:center;justify-content:center}

.hero{left:0;top:215px;width:1200px;height:479px;background:radial-gradient(ellipse at 50% 40%,#8a7a3a 0%,#4f6a2c 35%,#2f4a1f 70%,#24351a 100%)}
.hero-box{left:382px;top:115px;width:436px;height:251px;border:2px solid rgba(212,42,18,.8);background:rgba(40,30,20,.35);text-align:center;color:var(--white)}
.hero-box svg.train{display:block;margin:20px auto 0}
.hero-box h1{font-family:var(--slab);font-weight:400;font-size:29px;line-height:46px;margin-top:4px}
.hero-btn{display:inline-flex;align-items:center;gap:8px;margin-top:16px;background:var(--nav);color:var(--red);font-size:13px;padding:9px 18px}
.dots{display:flex;gap:6px}
.dots span{width:9px;height:9px;border-radius:50%;background:var(--white)}
.dots .on{background:var(--red)}

.welcome{left:0;top:694px;width:1200px;height:594px;background:var(--band);color:var(--white)}
.welcome h2{position:absolute;left:0;width:1200px;top:32px;text-align:center;font-family:var(--slab);font-weight:400;font-size:22px}
.welcome .sub{position:absolute;left:0;width:1200px;top:77px;text-align:center;font-size:12px;color:#9a9a9a;font-family:var(--slab);font-weight:300}
.card{position:absolute;top:122px;width:288px}
.card h3{color:var(--red);font-size:13px;font-weight:400;font-family:var(--slab);height:32px}
.card .photo{width:288px;height:203px}
.card p{font-size:11px;line-height:21px;margin-top:10px;color:#e6e6e6;text-align:justify}
.read{display:flex;align-items:center;height:41px;width:134px;margin-top:14px;background:#111;border-left:4px solid var(--red);color:var(--white);font-size:11.5px;padding-left:18px;clip-path:polygon(0 0,88% 0,100% 50%,88% 100%,0 100%)}

.instr{left:132px;top:1309px;width:384px}
.instr h2{font-family:var(--slab);font-weight:400;font-size:23px;line-height:31px}
.instr p{font-size:11px;line-height:21px;color:var(--muted);margin-top:14px;text-align:justify}
.instr ul{list-style:none;margin-top:20px}
.instr li{font-size:11px;color:var(--muted);height:34px;display:flex;gap:8px;white-space:nowrap}
.instr li::before{content:"";width:9px;height:11px;margin-top:3px;background:var(--red);border-radius:2px 2px 5px 5px;flex:none}
.instr .read{margin-top:12px}

.gallery-title{left:558px;top:1322px;font-family:var(--slab);font-size:23px;font-weight:400}
.arrows{left:1007px;top:1313px;display:flex;gap:2px}
.arrows span{width:29px;height:47px;background:#e3e3e3;display:flex;align-items:center;justify-content:center}
.tile{position:absolute;width:165px;height:97px}

.contact{left:0;top:1728px;width:1200px;height:377px}
.map{position:absolute;left:0;top:0;width:1200px;height:377px;background:linear-gradient(135deg,#eef0f4 0%,#e3e6ee 60%,#dfe3ea 100%)}
.map-tabs{position:absolute;left:356px;top:12px;background:var(--white);font-size:11px;padding:6px 10px;box-shadow:0 1px 3px rgba(0,0,0,.25)}
.map-tabs span{color:#888;margin-left:8px}
.contact-panel{position:absolute;left:0;top:0}
.contact-text{position:absolute;left:135px;top:114px;color:var(--white)}
.contact-text h2{font-family:var(--slab);font-weight:400;font-size:23px;margin-bottom:14px}
.contact-text .row{display:flex;gap:12px;font-size:15.5px;line-height:27px}
.contact-text svg{flex:none;margin-top:7px}

.partners-title{left:0;top:2136px;width:1200px;text-align:center;font-family:var(--slab);font-size:23px;font-weight:400}
.badge{position:absolute;top:2196px;width:121px;height:85px;background:var(--white);box-shadow:0 1px 4px rgba(0,0,0,.2);display:flex;align-items:center;justify-content:center}
.badge span{width:58px;height:58px;border-radius:50%;background:#8c8c8c}

.footer{left:0;top:2313px;width:1200px;height:43px;background:var(--footer);color:var(--white);font-size:12px}
.footer .copy{position:absolute;left:132px;top:13px}
.footer .social{left:952px;top:16px}
.footer .social i{border-color:var(--red)}
</style>
</head>
<body>

<div class="abs topbar">
  <div class="abs social"><i></i><i></i><i></i><i></i><i></i></div>
  <div class="abs info">&#9679; Crjr Company,Address name,City name. &nbsp;| &#9993; info@crjrmail.com</div>
</div>

<header class="abs header">
  <div class="abs logo">
    <div class="logo-mark"></div>
    <div class="logo-name">Cascade Ridge<br>Junction Railroad</div>
  </div>
  <div class="abs contact-btn"><div>CONTACT NOW :
    <svg width="11" height="11" viewBox="0 0 24 24"><path fill="#fff" d="M6.6 10.8a15 15 0 0 0 6.6 6.6l2.2-2.2c.3-.3.7-.4 1-.2 1.1.4 2.3.6 3.6.6.6 0 1 .4 1 1V20c0 .6-.4 1-1 1A17 17 0 0 1 3 4c0-.6.4-1 1-1h3.5c.6 0 1 .4 1 1 0 1.3.2 2.5.6 3.6.1.3 0 .7-.2 1z"/></svg>
    555-014-2290</div></div>
</header>

<nav class="abs nav">
  <a class="active" href="#">HOME</a>
  <a href="#" style="left:272px">ABOUT US</a>
  <a href="#" style="left:402px">OUR SERVICES</a>
  <a href="#" style="left:561px">INSTRUCTIONS</a>
  <a href="#" style="left:719px">GALLERY</a>
  <a href="#" style="left:840px">CONTACT US</a>
  <div class="abs search"><svg width="14" height="14" viewBox="0 0 24 24"><circle cx="10" cy="10" r="7" fill="none" stroke="#fff" stroke-width="3"/><path d="M15 15l7 7" stroke="#fff" stroke-width="3"/></svg></div>
</nav>

<section class="abs hero" role="img" aria-label="Locomotive approaching on a track through a green forest">
  <div class="abs hero-box">
    <svg class="train" width="34" height="36" viewBox="0 0 34 36"><rect x="3" y="2" width="28" height="24" rx="5" fill="#fff"/><rect x="8" y="7" width="18" height="8" fill="#3a2e20"/><circle cx="10" cy="20" r="2" fill="#3a2e20"/><circle cx="24" cy="20" r="2" fill="#3a2e20"/><path d="M8 27l-4 8M26 27l4 8" stroke="#fff" stroke-width="3"/></svg>
    <h1>CRJR<br>SHORT LINE RAIL ROAD</h1>
    <div class="hero-btn">ABOUT US
      <svg width="13" height="13" viewBox="0 0 24 24"><circle cx="12" cy="12" r="11" fill="#d42a12"/><path d="M10 7l5 5-5 5" stroke="#fff" stroke-width="3" fill="none"/></svg>
    </div>
  </div>
  <div class="abs dots" style="left:574px;top:447px"><span class="on"></span><span></span><span></span><span></span></div>
</section>

<section class="abs welcome">
  <h2>WELCOME TO CRJR</h2>
  <div class="sub">A COMPREHENSIVE RANGE OF RAIL ROAD SERVICES</div>
  <div class="card" style="left:132px">
    <h3>GOVERNMENT REGULATORS</h3>
    <div class="photo" role="img" aria-label="Modern tram at a city street stop" style="background:linear-gradient(180deg,#8fb3d9 0%,#b9bcc0 45%,#6f6c68 100%)"></div>
    <p>Lorem ipsum dolor sit amet, consectetur adipiscing elit. Aliquam lorem eros, placerat at nulla at, pulvinar porta elit. Pellentesque habitant morbi tristique senectus et netus.</p>
    <div class="read">Read more &nbsp;&raquo;</div>
  </div>
  <div class="card" style="left:456px">
    <h3>POTENTIAL NEW RAIL CUSTOMERS</h3>
    <div class="photo" role="img" aria-label="Red tram passing a brick building" style="background:linear-gradient(180deg,#8a5a40 0%,#a2574a 45%,#c62f36 70%,#7b7b7b 100%)"></div>
    <p>Lorem ipsum dolor sit amet, consectetur adipiscing elit. Aliquam lorem eros, placerat at nulla at, pulvinar porta elit. Pellentesque habitant morbi tristique senectus et netus.</p>
    <div class="read">Read more &nbsp;&raquo;</div>
  </div>
  <div class="card" style="left:779px">
    <h3>ECONOMIC DEVELOPMENT AGENCIES</h3>
    <div class="photo" role="img" aria-label="Train waiting at a station platform" style="background:linear-gradient(180deg,#d7d7d7 0%,#9c4a4a 40%,#8c8c8c 70%,#5f5f5f 100%)"></div>
    <p>Lorem ipsum dolor sit amet, consectetur adipiscing elit. Aliquam lorem eros, placerat at nulla at, pulvinar porta elit. Pellentesque habitant morbi tristique senectus et netus.</p>
    <div class="read">Read more &nbsp;&raquo;</div>
  </div>
  <div class="abs dots" style="left:585px;top:546px"><span class="on"></span><span style="background:#111"></span></div>
</section>

<section class="abs instr">
  <h2>INSTRUCTIONS FOR<br>THE GENERAL PUBLIC</h2>
  <p>Lorem ipsum dolor sit amet conse ctetur adipisicing elit, sed do eiusmod tempor incididunt ut labore et dolore magna aliqua. Ut enim ad minim veniam, quis nostrud exercitation ullamco laboris nisi ut aliquip ex ea commodo consequat.</p>
  <ul>
    <li>Lorem ipsum dolor sit amet, consectetur adipiscing elit. Aliquam</li>
    <li>Itant morbi tristique senectus et netus et malesuada fames ac turpis</li>
    <li>convallis dui, eget dictum diam pulvinar et. Sed auctor interdum</li>
    <li>ornare. Nulla urna ex, molestie quis dignissim sed, condimentum vel</li>
    <li>mauris. Curabitur molestie, purus nec eleifend ultrices, elit metus</li>
  </ul>
  <div class="read">Read more &nbsp;&raquo;</div>
</section>

<h2 class="abs gallery-title">OUR GALLERY</h2>
<div class="abs arrows">
  <span><svg width="10" height="12" viewBox="0 0 10 12"><path d="M7 1L2 6l5 5" stroke="#333" stroke-width="2" fill="none"/></svg></span>
  <span><svg width="10" height="12" viewBox="0 0 10 12"><path d="M3 1l5 5-5 5" stroke="#333" stroke-width="2" fill="none"/></svg></span>
</div>
<div class="tile" role="img" aria-label="Tram tracks in cobblestones" style="left:558px;top:1387px;background:linear-gradient(135deg,#8a7f76,#5d5650)"></div>
<div class="tile" role="img" aria-label="Rails glinting in sunlight" style="left:731px;top:1387px;background:linear-gradient(135deg,#e8e4da,#3a3834)"></div>
<div class="tile" role="img" aria-label="Modern tram at a platform" style="left:902px;top:1387px;background:linear-gradient(135deg,#9fb7cf,#8d8f91)"></div>
<div class="tile" role="img" aria-label="Green and white tram" style="left:558px;top:1492px;background:linear-gradient(135deg,#b7c27a,#5d6460)"></div>
<div class="tile" role="img" aria-label="Blue and white tram front" style="left:731px;top:1492px;background:linear-gradient(135deg,#5d84c4,#dfe3e8)"></div>
<div class="tile" role="img" aria-label="Tram on a city street" style="left:902px;top:1492px;background:linear-gradient(135deg,#8aa6c5,#a79f8e)"></div>
<div class="tile" role="img" aria-label="Crowd at a tram stop" style="left:558px;top:1598px;background:linear-gradient(135deg,#7e7570,#c6c2bc)"></div>
<div class="tile" role="img" aria-label="Tram in a town square" style="left:731px;top:1598px;background:linear-gradient(135deg,#9b6a55,#6e86a8)"></div>
<div class="tile" role="img" aria-label="Track maintenance work" style="left:902px;top:1598px;background:linear-gradient(135deg,#6c7b8c,#9c9486)"></div>

<section class="abs contact">
  <div class="map" role="img" aria-label="Map of the railroad line and surrounding area"></div>
  <div class="map-tabs">Map<span>Satellite</span></div>
  <svg class="contact-panel" width="1200" height="377" viewBox="0 0 1200 377"><polygon points="0,0 298,0 480,377 0,377" fill="#d42a12"/></svg>
  <div class="contact-text">
    <h2>CONTACT US</h2>
    <div class="row"><svg width="11" height="14" viewBox="0 0 12 16"><path d="M6 0a6 6 0 0 0-6 6c0 4.5 6 10 6 10s6-5.5 6-10a6 6 0 0 0-6-6zm0 8.5A2.5 2.5 0 1 1 6 3.5a2.5 2.5 0 0 1 0 5z" fill="#fff"/></svg><div>4810 Alder Ridge Rd Suite 200,<br>Fernvale, WA 98990,<br>United States</div></div>
    <div class="row"><svg width="14" height="11" viewBox="0 0 16 12"><rect width="16" height="12" rx="1" fill="#fff"/><path d="M0 1l8 6 8-6" stroke="#d42a12" stroke-width="1.5" fill="none"/></svg><div>info@crjrcompanymail.com</div></div>
    <div class="row"><svg width="13" height="13" viewBox="0 0 24 24"><path fill="#fff" d="M6.6 10.8a15 15 0 0 0 6.6 6.6l2.2-2.2c.3-.3.7-.4 1-.2 1.1.4 2.3.6 3.6.6.6 0 1 .4 1 1V20c0 .6-.4 1-1 1A17 17 0 0 1 3 4c0-.6.4-1 1-1h3.5c.6 0 1 .4 1 1 0 1.3.2 2.5.6 3.6.1.3 0 .7-.2 1z"/></svg><div>+1 555-014-2290</div></div>
  </div>
</section>

<h2 class="abs partners-title">OUR PARNTERS</h2>
<div class="badge" style="left:132px" aria-label="Harlow County Washington"><span></span></div>
<div class="badge" style="left:267px" aria-label="Port of Elmstead (Washington)"><span></span></div>
<div class="badge" style="left:404px" aria-label="MVBTA"><span style="border-radius:4px;width:70px;height:30px"></span></div>
<div class="badge" style="left:539px" aria-label="City of Pinecrest Hollow"><span></span></div>
<div class="badge" style="left:676px" aria-label="National Trackway Bureau"><span></span></div>
<div class="badge" style="left:811px" aria-label="QBO"><span></span></div>
<div class="badge" style="left:947px" aria-label="HPMRA"><span style="background:#222"></span></div>

<footer class="abs footer">
  <div class="copy">Cascade Ridge junction rail road &copy; 2016. Privacy policy</div>
  <div class="abs social"><i></i><i></i><i></i><i></i><i></i></div>
</footer>

</body>
</html>
```